Talwick Orsine Beauty brand redesign of product labels

national rebrand of skincare product labels - same design but 6 sizes. Will be used for facial serums, body oils, bath salts, room sprays, etc. All labels to be same design - just adjusted for the different sizes. See brand document and sample label.

Bottle Specifications are located in the branding file.
Fonts included in product branding document.
Colours included in branding document.

Featuring company name and logo, product name, product feature, ingredients, size, directions, tag line. See attached sample label as example for design.

Black label base - matt.

Target Market(s)

Natural beauty, 20-60

Industry/Entity Type

farming, natural beauty

Font styles to use
Sans Serif

Requirements
Must have
• Modern, clean, homey
Nice to have
• modern clean design - using the branding colours provided
Should not have
• busy, crowded,

```html
<!DOCTYPE html>
<html lang="en">
<head>
<meta charset="utf-8">
<title>Talwick Orsine Beauty – Mirelle Skin Repair Label</title>
<link rel="stylesheet" href="https://fonts.googleapis.com/css2?family=Open+Sans:wght@300;400;600&family=Great+Vibes&display=swap">
<style>
  :root {
    --page: #ffffff;
    --label-base: #2b2527;
    --floral-tone: #3a3235;
    --mauve: #a79ba1;
    --cream: #f3ece3;
    --soft-grey: #b5abaf;
  }
  * { margin: 0; padding: 0; box-sizing: border-box; }
  html, body {
    width: 1200px; height: 1200px; overflow: hidden;
    background: var(--page);
  }
  .canvas { position: relative; width: 1200px; height: 1200px; }

  .label {
    position: absolute; left: 50px; top: 326px;
    width: 1100px; height: 548px;
    background: var(--label-base);
    overflow: hidden;
    font-family: "Open Sans", sans-serif;
  }

  .tagline {
    position: absolute; left: 46px; top: 40px; height: 472px;
    writing-mode: vertical-rl; transform: rotate(180deg);
    text-align: center;
    color: var(--soft-grey); font-weight: 300; font-size: 20px;
    letter-spacing: 0.5px; white-space: nowrap;
  }

  .floral { position: absolute; border-radius: 40% 50% 45% 55%; background: var(--floral-tone); }
  .floral-top { left: 229px; top: -10px; width: 275px; height: 330px; }
  .floral-bottom { left: 637px; top: 242px; width: 268px; height: 320px; }

  .brand-name {
    position: absolute; left: 440px; top: 72px; width: 220px;
    display: flex; align-items: center; justify-content: center; gap: 10px;
    color: var(--cream); font-weight: 400; font-size: 13px;
    letter-spacing: 2px; line-height: 1.35; text-transform: uppercase;
    text-align: center;
  }
  .brand-dot {
    width: 10px; height: 10px; border-radius: 50%;
    background: var(--cream); flex: none;
  }

  .product-name {
    position: absolute; left: 348px; top: 190px; width: 400px;
    text-align: center;
    font-family: "Great Vibes", cursive; font-size: 92px; font-weight: 400;
    color: var(--mauve); line-height: 1;
  }

  .feature-band {
    position: absolute; left: 311px; top: 336px;
    width: 476px; height: 69px;
    background: var(--mauve);
    display: flex; flex-direction: column; align-items: center; justify-content: center;
    color: var(--cream); font-weight: 600; font-size: 19px;
    line-height: 1.4; letter-spacing: 0.3px; text-transform: uppercase;
  }

  .benefit {
    position: absolute; left: 311px; top: 416px; width: 476px;
    text-align: center; color: var(--cream);
    font-weight: 400; font-size: 26px; letter-spacing: 0.8px;
  }

  .net-volume {
    position: absolute; left: 311px; top: 510px; width: 476px;
    text-align: center; color: var(--cream);
    font-weight: 400; font-size: 11px;
  }
</style>
</head>
<body>
<main class="canvas">
  <section class="label">
    <p class="tagline">grown with care, from field to skin</p>

    <div class="floral floral-top" role="img" aria-label="Line-drawn botanical illustration of dahlias, buds and leafy stems"></div>
    <div class="floral floral-bottom" role="img" aria-label="Line-drawn botanical illustration of a dahlia with berry sprigs and buds"></div>

    <div class="brand-name">
      <span class="brand-dot"></span>
      <span>Talwick<br>Orsine<br>Beauty</span>
    </div>

    <h1 class="product-name">Mirelle</h1>

    <div class="feature-band">
      <span>Concentrated</span>
      <span>Hialuronic Acid Gel</span>
    </div>

    <p class="benefit">SKIN REPAIR</p>

    <p class="net-volume">net 6,8 oz | 200 ml</p>
  </section>
</main>
</body>
</html>
```